Online Bonuses Website Logo / Header Design

I need a header designing for a new Wordpress website. Your design must be sized 970px x 250px.

For an example the image below was for a logo / header design for a cycling website.

http://www.pedalgazette.example/wp-content/uploads/2015/01/PedalGazette-Header11.jpg

Which fitted into the Wordpress website as below:

http://www.pedalgazette.example/

Now though, for this design I need a header for an online gambling website.

The website will be called Prize Pardner and will offer its readers online offers for:

Bingo Bonuses
Poker Bonuses
Casino Bonuses
Sports Betting Bonuses
Special Bonuses

I have no set colour scheme or design in mind. I’m also open to all ideas.

One idea I do like is something similar to the header of http://www.quillsgadgetbarn.example/ but using different cartoon Mexican characters. With each different character holding a board that displays the bonus, such as Bingo Bonus, poker bonus etc etc. To the left of the characters display the website name Prize Pardner.

However, as I have said I'm open to YOUR ideas for the header.

Remember though the main goal of the header is to instantly let the "viewer" know what the website is all about.

Your image must be fully layered and you must supply any fonts used etc, so I can load the image in photoshop.
Updates

Target Market(s)

Online Gambling

Industry/Entity Type

Online

Logo Text

Only The Best Online Gambling Bonuses!

Logo styles of interest
Character Logo
Requirements
Must have
• Your design must instantly tell the viewer what the website is all about.
Nice to have
• A character or characters as per the brief but not essential.
Should not have
• Too much text

```html
<!DOCTYPE html>
<html lang="en">
<head>
<meta charset="utf-8">
<title>Prize Pardner — Header</title>
<link rel="stylesheet" href="https://fonts.googleapis.com/css2?family=Roboto:wght@700;900&display=swap">
<style>
  :root {
    --sky: #12b4da;
    --sky-deep: #0aa3c9;
    --sky-glow: #22c3e6;
    --gold-light: #f6dfb0;
    --gold: #d9a86a;
    --gold-dark: #a9713a;
    --gold-ink: #7a4a1c;
    --white: #ffffff;
  }
  html, body {
    margin: 0;
    padding: 0;
    width: 1200px;
    height: 309px;
    overflow: hidden;
    background: var(--sky);
  }
  .header {
    position: relative;
    width: 1200px;
    height: 309px;
    overflow: hidden;
    background: radial-gradient(ellipse at 30% 40%, var(--sky-glow) 0%, var(--sky) 55%, var(--sky-deep) 100%);
    font-family: "Roboto", Arial, sans-serif;
  }
  .coin-pile {
    position: absolute;
    left: 20px;
    top: 160px;
    width: 500px;
    height: 149px;
    background: radial-gradient(ellipse 50% 60% at 50% 60%,
      rgba(246, 223, 176, 0.95) 0%,
      rgba(217, 168, 106, 0.85) 45%,
      rgba(169, 113, 58, 0.45) 75%,
      rgba(169, 113, 58, 0) 100%);
  }
  .brand {
    position: absolute;
    left: 142px;
    top: 30px;
    margin: 0;
    color: var(--white);
    font-weight: 900;
    font-size: 58px;
    line-height: 0.95;
    text-transform: uppercase;
    letter-spacing: 1px;
  }
  .bonus-list {
    list-style: none;
    margin: 0;
    padding: 0;
  }
  .bonus-item {
    position: absolute;
    display: flex;
    align-items: center;
    gap: 16px;
    color: var(--white);
    font-weight: 700;
    font-size: 20px;
    letter-spacing: 0.3px;
    text-transform: uppercase;
    white-space: nowrap;
  }
  .bonus-icon { width: 50px; height: 50px; flex: none; }
  .item-bingo   { left: 566px; top: 59px; }
  .item-poker   { left: 872px; top: 59px; }
  .item-sports  { left: 566px; top: 134px; }
  .item-casino  { left: 872px; top: 134px; }
  .item-special { left: 566px; top: 209px; }
  .cta {
    position: absolute;
    left: 866px;
    top: 213px;
    width: 340px;
    height: 100px;
    box-sizing: border-box;
    padding: 18px 0 0 24px;
    background: linear-gradient(160deg, var(--gold-light) 0%, var(--gold) 55%, var(--gold-dark) 100%);
    color: var(--gold-ink);
    font-weight: 900;
    font-size: 27px;
    line-height: 1.05;
    text-decoration: none;
    white-space: nowrap;
  }
</style>
</head>
<body>
<header class="header">
  <div class="coin-pile" role="img" aria-label="Pile of scattered gold bonus coins"></div>
  <h1 class="brand">Prize<br>Pardner</h1>

  <ul class="bonus-list">
    <li class="bonus-item item-bingo">
      <svg class="bonus-icon" viewBox="0 0 50 50" aria-hidden="true">
        <circle cx="25" cy="25" r="24" fill="var(--gold)" stroke="var(--gold-light)" stroke-width="2"/>
        <text x="25" y="32" text-anchor="middle" font-family="Roboto, Arial, sans-serif" font-weight="700" font-size="18" fill="var(--gold-ink)">15</text>
      </svg>
      Bingo Bonuses
    </li>
    <li class="bonus-item item-poker">
      <svg class="bonus-icon" viewBox="0 0 50 50" aria-hidden="true">
        <circle cx="25" cy="25" r="24" fill="var(--gold)" stroke="var(--gold-light)" stroke-width="2"/>
        <circle cx="25" cy="25" r="15" fill="none" stroke="var(--gold-ink)" stroke-width="2" stroke-dasharray="5 4"/>
        <circle cx="25" cy="25" r="8" fill="none" stroke="var(--gold-ink)" stroke-width="2"/>
      </svg>
      Poker Bonuses
    </li>
    <li class="bonus-item item-sports">
      <svg class="bonus-icon" viewBox="0 0 50 50" aria-hidden="true">
        <circle cx="25" cy="25" r="24" fill="var(--gold)" stroke="var(--gold-light)" stroke-width="2"/>
        <path d="M12 20 h18 a9 9 0 1 1 -9 9 h-9 z" fill="none" stroke="var(--gold-ink)" stroke-width="2.5" stroke-linejoin="round"/>
      </svg>
      Sports Bonuses
    </li>
    <li class="bonus-item item-casino">
      <svg class="bonus-icon" viewBox="0 0 50 50" aria-hidden="true">
        <circle cx="25" cy="25" r="24" fill="var(--gold)" stroke="var(--gold-light)" stroke-width="2"/>
        <rect x="11" y="17" width="28" height="16" rx="2" fill="none" stroke="var(--gold-ink)" stroke-width="2.5"/>
        <path d="M20.5 17 v16 M29.5 17 v16" stroke="var(--gold-ink)" stroke-width="2"/>
      </svg>
      Cassino Bonuses
    </li>
    <li class="bonus-item item-special">
      <svg class="bonus-icon" viewBox="0 0 50 50" aria-hidden="true">
        <circle cx="25" cy="25" r="24" fill="var(--gold)" stroke="var(--gold-light)" stroke-width="2"/>
        <path d="M25 10 l4.4 9.6 10.4 1.1 -7.8 7 2.3 10.3 -9.3 -5.4 -9.3 5.4 2.3 -10.3 -7.8 -7 10.4 -1.1 z" fill="var(--gold-ink)"/>
      </svg>
      Special Bonuses
    </li>
  </ul>

  <a class="cta" href="#">Click here<br>and get lucky &gt;&gt;&gt;</a>
</header>
</body>
</html>
```